Corvanta Stationery Design

We need design for our stationary, including:
1) Letterhead
- A4/Letter size in landscape and portrait letterhead
- The letterhead must be in a word file, and the address should be editable using the Felixti or Perpetua Titling TTF
- The output file should be in .docx and in .ai.
2) Business card
- The business card will be printed in white paper and single face only, so there should be nothing on the reverse side.
3) Envelope (sizes A4, Letter, and small document)
Please refer to the picture showing some samples of stationary with designs that would fulfill our wish.
We're including the logo in .AI.
Thanks
Target Market(s)
High end investors
Industry/Entity Type
Landscape
Look and feel
Each slider illustrates characteristics of the customer's brand and the style your logo design should communicate.

```html
<!DOCTYPE html>
<html lang="en">
<head>
<meta charset="utf-8">
<title>Corvanta Capital Partners — Letterhead</title>
<link rel="stylesheet" href="https://fonts.googleapis.com/css2?family=Cinzel:wght@700&display=swap">
<style>
  :root {
    --paper: #ffffff;
    --brand-teal: #0899c0;
    --ink: #2a2a2a;
    --footer-text: #ffffff;
  }
  html, body {
    margin: 0;
    padding: 0;
    overflow: hidden;
    background: var(--paper);
  }
  .letterhead {
    position: relative;
    width: 1200px;
    height: 849px;
    background: var(--paper);
    overflow: hidden;
  }
  .company-name {
    position: absolute;
    top: 60px;
    right: 34px;
    margin: 0;
    font-family: 'Cinzel', serif;
    font-weight: 700;
    font-size: 20px;
    line-height: 24px;
    color: var(--ink);
    white-space: nowrap;
  }
  .footer-band {
    position: absolute;
    left: 0;
    bottom: 0;
    width: 1200px;
    height: 100px;
  }
  .footer-band svg {
    display: block;
  }
  .footer-contact {
    position: absolute;
    left: 0;
    bottom: 24px;
    width: 1162px;
    margin: 0;
    text-align: center;
    font-family: 'Cinzel', serif;
    font-weight: 700;
    font-size: 16px;
    line-height: 20px;
    color: var(--footer-text);
    letter-spacing: 0.2px;
  }
</style>
</head>
<body>
  <main class="letterhead">
    <header>
      <p class="company-name">Corvanta Capital Partners</p>
    </header>

    <footer class="footer-band">
      <svg width="1200" height="100" viewBox="0 0 1200 100" aria-hidden="true">
        <path d="M0 35 Q600 -27 1200 35 L1200 100 L0 100 Z" fill="var(--brand-teal)"/>
      </svg>
      <p class="footer-contact">
        This is our address, write to us here, call us here<br>
        Email us here, check our website here.
      </p>
    </footer>
  </main>
</body>
</html>
```